BriMora Journeys Business Card Design

We need a new business card design for our travel agency business - BriMora Journeys. We design packages to some of the most popular travel destinations in the world for groups, individuals and also tailor-make personalised packages. Our logo attached must be used. On the back of the card we would like a list of all websites under our BriMora brand to be posted. We would like clean, modern, simple design.

Industry/Entity Type

Travel Agent

Contact Information for Business Card

Owen Farrant
National Sales Manager
Reservations: 1300 527 649
Tel: 61 28473 5961
Fax: 61 2847 3907
Email: owen@brimorajourneys.com.au
Web: www.brimorajourneys.com.au

Address: Level 1, 417 Harwood Street
Sydney NSW 2000 Australia

Requirements
Must have
• On the back of the card we want all websites listed under our BriMora brand.
• BriMora Journeys Group - Wholesale Specialists
• www.kpwander.com.au - New Caledonia
• www.islebreeze.com.au - Tahiti
• www.orientjourneyhub.com.au - China
Nice to have
• Modern, clean lined, simple and fresh
Should not have
• Look dull

```html
<!DOCTYPE html>
<html lang="en">
<head>
<meta charset="utf-8">
<title>BriMora Journeys Business Card</title>
<link rel="stylesheet" href="https://fonts.googleapis.com/css2?family=Lato:wght@400;700&display=swap">
<style>
  :root {
    --navy: #2b2a7e;
    --red: #e8222b;
    --paper: #ffffff;
    --backdrop: #e9e7e3;
    --plane-tint: #f6dcd2;
  }
  * { margin: 0; padding: 0; box-sizing: border-box; }
  html, body { width: 1200px; height: 800px; overflow: hidden; }
  body {
    background: var(--backdrop);
    font-family: "Lato", Arial, sans-serif;
    display: flex;
    align-items: center;
    justify-content: center;
    gap: 40px;
  }
  .card {
    position: relative;
    width: 540px;
    height: 300px;
    background: var(--paper);
    box-shadow: 0 6px 18px rgba(0,0,0,0.18);
    overflow: hidden;
  }
  .swoosh { position: absolute; inset: 0; width: 100%; height: 100%; }
  .plane-shape {
    position: absolute;
    left: 250px; top: 150px;
    width: 150px; height: 110px;
    background: radial-gradient(ellipse at center, var(--plane-tint) 0%, rgba(246,220,210,0) 70%);
  }
  .brand-name {
    font-weight: 700;
    color: var(--navy);
    white-space: nowrap;
  }
  .front .brand-block {
    position: absolute;
    right: 20px; top: 22px;
    text-align: right;
  }
  .front .brand-name { font-size: 30px; line-height: 1; }
  .rule { height: 1px; background: var(--navy); margin: 6px 0 6px auto; width: 100%; }
  .address { font-size: 12px; color: var(--navy); line-height: 1.35; }
  .contact {
    position: absolute;
    left: 24px; top: 150px;
    color: var(--navy);
  }
  .person-name { font-size: 22px; font-weight: 700; color: var(--red); line-height: 1.1; }
  .person-role, .reservations { font-size: 12px; line-height: 1.35; }
  .contact-list { list-style: none; margin-top: 8px; }
  .contact-list li {
    display: flex; align-items: center; gap: 7px;
    font-size: 12px; line-height: 1.45;
  }
  .contact-list svg { width: 11px; height: 11px; flex: none; }

  .back {
    display: flex; flex-direction: column;
    align-items: center; justify-content: center;
    text-align: center;
  }
  .back .brand-name { font-size: 38px; line-height: 1; }
  .back .rule { width: 300px; margin: 10px auto 22px; }
  .group-line { font-size: 14px; color: var(--red); line-height: 1.45; }
  .site-list { list-style: none; font-size: 14px; color: var(--navy); line-height: 1.45; }
</style>
</head>
<body>
  <section class="card front" aria-label="Card front">
    <svg class="swoosh" viewBox="0 0 540 300" preserveAspectRatio="none" aria-hidden="true">
      <path d="M0,78 C200,56 420,110 540,300 C400,140 200,104 0,106 Z" fill="var(--red)"/>
      <path d="M0,110 C200,108 400,146 540,300 C390,158 200,120 0,117 Z" fill="var(--navy)"/>
    </svg>
    <div class="plane-shape" role="img" aria-label="Faint aeroplane decoration"></div>
    <div class="brand-block">
      <div class="brand-name">BriMora Journeys</div>
      <div class="rule"></div>
      <p class="address">Level 1, 417 Harwood Street<br>Sydney NSW 2000 Australia</p>
    </div>
    <div class="contact">
      <p class="person-name">Owen Farrant</p>
      <p class="person-role">National Sales Manager</p>
      <p class="reservations">Reservations: 1300 527 649</p>
      <ul class="contact-list">
        <li><svg viewBox="0 0 12 12"><path d="M1 4 C1 2 3 1 6 1 C9 1 11 2 11 4 L8.5 4.5 L8 3 L4 3 L3.5 4.5 Z M3 6 L9 6 L10.5 11 L1.5 11 Z" fill="var(--red)"/></svg>61 28473 5961</li>
        <li><svg viewBox="0 0 12 12"><rect x="3" y="1" width="6" height="4" fill="var(--red)"/><rect x="1" y="5" width="10" height="5" rx="1" fill="var(--red)"/><rect x="3" y="8" width="6" height="3" fill="#fff" stroke="var(--red)"/></svg>61 2847 3907</li>
        <li><svg viewBox="0 0 12 12"><rect x="0.5" y="2" width="11" height="8" fill="var(--red)"/><path d="M0.5 2 L6 6.5 L11.5 2" fill="none" stroke="#fff" stroke-width="1"/></svg>owen@brimorajourneys.com.au</li>
        <li><svg viewBox="0 0 12 12"><circle cx="6" cy="6" r="5.5" fill="var(--red)"/><path d="M0.5 6 H11.5 M6 0.5 V11.5 M6 0.5 C3 3 3 9 6 11.5 M6 0.5 C9 3 9 9 6 11.5" fill="none" stroke="#fff" stroke-width="0.8"/></svg>www.brimorajourneys.com.au</li>
      </ul>
    </div>
  </section>

  <section class="card back" aria-label="Card back">
    <div class="brand-name">BriMora Journeys</div>
    <div class="rule"></div>
    <p class="group-line">BriMora Journeys Group - Wholesale Specialists</p>
    <ul class="site-list">
      <li>www.kpwander.com.au - New Caledonia</li>
      <li>www.islebreeze.com.au - Tahiti</li>
      <li>www.orientjourneyhub.com.au - China</li>
    </ul>
  </section>
</body>
</html>
```